conférence Débat Innovation
Bonjour,
Dans le cadre de l'organisation d'un événement institutionnel, je suis à la recherche d'un professionnel graphiste pour la création des supports suivants :
- flyer de l'événement (pour web et print),
- version pour les réseaux sociaux et le site internet de l'événement,
- flyer de cet événement personnalisé pour un concours dont la finale aura lieu le jour de l'événement,
- version affiches pour le jour J,
- Carton d'invitation pour mailing et impression.
L'événement est une conférence débat sur l'entreprenariat et l'innovation en banlieue parisienne.
L'idée est de dynamiser un territoire et le mettre en avant ses atouts.

```html
<!DOCTYPE html>
<html lang="fr">
<head>
<meta charset="utf-8">
<title>Conférence Débat – Entreprenariat & Innovation</title>
<link rel="stylesheet" href="https://fonts.googleapis.com/css2?family=Cinzel:wght@400;700&family=Josefin+Sans:wght@100;300;400;600&family=Poiret+One&display=swap">
<style>
  :root {
    --sky-top: #c3cedb;
    --sky-mid: #8499b2;
    --sky-deep: #6f86a2;
    --sky-bottom: #a9b6c8;
    --white: #ffffff;
    --title-grey: #8893a1;
    --title-dark: #5a6471;
    --ink: #3c4350;
    --accent: #d9834a;
    --accent-deep: #c0622f;
    --badge: rgba(222, 228, 238, 0.62);
  }
  * { margin: 0; padding: 0; box-sizing: border-box; }
  html, body { width: 801px; height: 1200px; overflow: hidden; }
  body { background: var(--sky-mid); }
  .poster {
    position: relative;
    width: 801px;
    height: 1200px;
    overflow: hidden;
    background:
      radial-gradient(ellipse 60% 30% at 30% 40%, rgba(255,255,255,0.22), transparent 70%),
      radial-gradient(ellipse 70% 25% at 70% 75%, rgba(255,255,255,0.2), transparent 70%),
      linear-gradient(180deg, var(--sky-top) 0%, var(--sky-mid) 30%, var(--sky-deep) 55%, var(--sky-mid) 75%, var(--sky-bottom) 100%);
    text-align: center;
  }
  .event-type {
    position: absolute; top: 52px; left: 0; right: 0;
    font-family: "Josefin Sans", sans-serif; font-weight: 100;
    font-size: 54px; letter-spacing: 5px; color: var(--white);
  }
  .headline {
    position: absolute; top: 222px; left: 0; right: 0;
    font-family: "Poiret One", sans-serif; line-height: 1.05;
    font-size: 76px; text-shadow: 0 2px 6px rgba(40,50,65,0.45);
  }
  .headline .line-1 { display: block; color: var(--title-grey); }
  .headline .line-2 { display: block; color: var(--title-dark); font-size: 80px; }
  .location-tag {
    position: absolute; top: 422px; left: 0; right: 0;
    font-family: "Josefin Sans", sans-serif; font-weight: 300;
    font-size: 19px; letter-spacing: 1px; color: var(--white);
  }
  .idea-art {
    position: absolute; left: 85px; top: 490px; width: 260px; height: 300px;
    border-radius: 50% 50% 40% 40%;
    background: radial-gradient(ellipse at 50% 40%, rgba(255,255,255,0.28), rgba(255,255,255,0) 70%);
  }
  .contest-badge {
    position: absolute; left: 513px; top: 473px; width: 254px; height: 254px;
    border-radius: 50%; background: var(--badge);
    display: flex; align-items: center; justify-content: center;
  }
  .contest-badge p {
    transform: rotate(18deg);
    font-family: "Cinzel", serif; font-weight: 400;
    font-size: 29px; line-height: 1.35; color: var(--accent-deep);
  }
  .tagline, .closing {
    position: absolute; left: 0; right: 0;
    font-family: "Cinzel", serif; font-weight: 700;
    font-size: 25px; letter-spacing: 1px; color: var(--accent);
  }
  .tagline { top: 880px; }
  .closing { top: 1127px; }
  .rule {
    position: absolute; left: 73px; width: 655px; height: 2px;
    background: rgba(255,255,255,0.85);
  }
  .rule.top { top: 933px; }
  .rule.bottom { top: 1087px; }
  .details {
    position: absolute; top: 968px; left: 0; right: 0;
    font-family: "Josefin Sans", sans-serif; font-weight: 600;
    font-size: 34px; line-height: 58px; color: var(--ink);
  }
  .details .soft { color: #eef2f7; }
  .details .muted { color: #5d6674; }
</style>
</head>
<body>
  <main class="poster">
    <h2 class="event-type">CONFERENCE DEBAT</h2>
    <h1 class="headline">
      <span class="line-1">ENTREPRENARIAT &amp;</span>
      <span class="line-2">INNOVATION</span>
    </h1>
    <p class="location-tag">EN BANLIEUE PARISIENNE</p>

    <div class="idea-art" role="img" aria-label="Line drawing of a glowing light bulb symbolising a new idea"></div>

    <div class="contest-badge">
      <p>CONCOURS<br>START UP<br>2016</p>
    </div>

    <p class="tagline">INNOVATION . JEUNESSE . OPPORTUNITE</p>
    <div class="rule top"></div>
    <div class="details">
      <div>21 SEPT. 2016 A PARTIR DE <span class="soft">10H30</span></div>
      <div><span class="soft">FORUM DES RENCONTRES</span> <span class="muted">PARIS</span></div>
    </div>
    <div class="rule bottom"></div>
    <p class="closing">MOMENT UNIQUE OUVERT A TOUS</p>
  </main>
</body>
</html>
```